Lantern Airfields Homepage Design Update

here's the current site - http://lanternairfields.example/

client is not happy with overall look.

keeping the same info - intro text, headlines, featured media excepts and general navigation options - can you come up with a nicer, slicker look for this homepage?

UPDATE: since it was asked by designer.. the general layout doesnt have to be the same. its not required to have a big image, with text below that and then smaller images/text below that. as long as we have the same content on the page, it can organized and designed in any way,

client like big images, so one way or the other, keep that... but feel free to reorganize content, explore different ways of framing it, and/or anything else. make this homepage pop!

for the designer that wins this, we'll start an additional project to update the interior.

let me know if any questions..

thanks!

marcus

Target Market(s)

aviation industry professionals, local governments, general public

Number of Pages Required

1 page

Font styles to use
Sans Serif

Requirements
Must have
• big image somewhere. same content as on current site, just designed differently.

```html
<!DOCTYPE html>
<html lang="en">
<head>
<meta charset="utf-8">
<title>Lantern Airfields — Home</title>
<link href="https://fonts.googleapis.com/css2?family=Open+Sans:wght@400;600;700&display=swap" rel="stylesheet">
<style>
  :root {
    --brand-blue: #193a9c;
    --brand-green: #8cc21b;
    --ink: #1c1c1c;
    --muted: #6b6b6b;
    --rule: #1f3f6e;
    --white: #ffffff;
    --night: #050505;
  }
  * { box-sizing: border-box; margin: 0; padding: 0; }
  html, body { width: 1200px; height: 900px; overflow: hidden; background: var(--white); }
  body { font-family: "Open Sans", Arial, sans-serif; position: relative; color: var(--ink); }

  .site-header { position: absolute; top: 0; left: 0; width: 1200px; height: 75px; background: var(--white); }
  .brand { position: absolute; left: 166px; top: 26px; display: flex; align-items: center; gap: 8px; text-decoration: none; }
  .brand-dot { width: 14px; height: 14px; border-radius: 50%; background: var(--brand-blue); }
  .brand-name { font-size: 15px; font-weight: 400; color: var(--brand-blue); letter-spacing: .3px; }

  .main-nav { position: absolute; top: 0; left: 526px; display: flex; height: 75px; }
  .main-nav a { display: flex; align-items: center; height: 75px; padding: 0 12px; margin-right: 2px;
    font-size: 12px; font-weight: 400; color: #222; text-decoration: none; letter-spacing: .4px; }
  .main-nav a.is-active { background: var(--brand-blue); color: var(--white); }

  .hero { position: absolute; top: 75px; left: 0; width: 1200px; height: 497px;
    background:
      radial-gradient(ellipse 420px 200px at 150px 380px, rgba(255,255,255,.85), transparent 70%),
      radial-gradient(ellipse 300px 80px at 600px 500px, rgba(255,255,255,.95), transparent 70%),
      radial-gradient(ellipse 300px 120px at 1050px 330px, rgba(255,255,255,.7), transparent 70%),
      linear-gradient(180deg, #b9d8f4 0%, #a9cdf0 55%, #c4dcf2 100%); }

  .welcome { position: absolute; top: 572px; left: 0; width: 1200px; text-align: center; }
  .welcome-title { margin-top: 65px; font-size: 22px; font-weight: 700; letter-spacing: 2.6px; color: var(--ink); }
  .welcome-title span { color: var(--brand-green); }
  .divider { display: block; margin: 6px auto 0; }
  .welcome-text { margin-top: 18px; font-size: 12px; line-height: 18px; letter-spacing: .6px; color: var(--muted); }

  .actions { margin-top: 21px; display: flex; justify-content: center; gap: 11px; }
  .btn { display: flex; align-items: center; justify-content: center; width: 112px; height: 37px;
    font-size: 12px; letter-spacing: .6px; text-decoration: none; box-shadow: 0 3px 6px rgba(0,0,0,.18); }
  .btn-primary { background: var(--brand-blue); color: var(--white); }
  .btn-outline { border: 2px solid var(--brand-green); color: var(--brand-green); background: var(--white); }

  .feature-strip { position: absolute; top: 875px; left: 0; width: 1200px; height: 25px; display: flex; }
  .feature-strip .media { width: 600px; background: var(--night); }
  .feature-strip .panel { width: 600px; background: var(--brand-blue); }
</style>
</head>
<body>
  <header class="site-header">
    <a class="brand" href="http://lanternairfields.example/">
      <span class="brand-dot"></span>
      <span class="brand-name">Lantern Airfields</span>
    </a>
    <nav class="main-nav">
      <a class="is-active" href="#">HOME</a>
      <a href="#">ABOUT US</a>
      <a href="#">AIRPORTS</a>
      <a href="#">NEWS AND MEDIA</a>
      <a href="#">CONTACT US</a>
      <a href="#">EMPLOYEES</a>
    </nav>
  </header>

  <section class="hero" role="img" aria-label="Photo of a passenger jet flying overhead against a blue sky with white clouds"></section>

  <section class="welcome">
    <h1 class="welcome-title">WELCOME TO <span>LANTERN AIRFIELDS</span></h1>
    <svg class="divider" width="226" height="20" viewBox="0 0 226 20" aria-hidden="true">
      <line x1="0" y1="10" x2="104" y2="10" stroke="var(--rule)" stroke-width="1.5"/>
      <line x1="122" y1="10" x2="226" y2="10" stroke="var(--rule)" stroke-width="1.5"/>
      <rect x="107" y="4" width="12" height="12" transform="rotate(45 113 10)" fill="#fff" stroke="var(--rule)" stroke-width="1.5"/>
    </svg>
    <p class="welcome-text">Bringing private, free enterprise business practices<br>To airports throughout the U.S.</p>
    <div class="actions">
      <a class="btn btn-primary" href="#">about us</a>
      <a class="btn btn-outline" href="#">service</a>
    </div>
  </section>

  <div class="feature-strip">
    <div class="media" role="img" aria-label="Dark featured media image"></div>
    <div class="panel"></div>
  </div>
</body>
</html>
```